Im opening up a plumbing business and would like a young modern attractive logo I like bright blues and greens and also like environmentally friendly things

Business

Tallow Creek plumbing and gas

```html
<!DOCTYPE html>
<html lang="en">
<head>
<meta charset="utf-8">
<title>Tallow Creek Plumbing and Gas – Business Card</title>
<link rel="stylesheet" href="https://fonts.googleapis.com/css2?family=Raleway:wght@300;800&family=Zilla+Slab:wght@700&display=swap">
<style>
  :root {
    --backdrop: #4e7b98;
    --card-deep: #1f4662;
    --card-mid: #2b5a78;
    --card-light: #376a88;
    --brand-green: #d4ecb0;
    --contact-white: #e6eff3;
  }
  * { margin: 0; padding: 0; box-sizing: border-box; }
  html, body {
    width: 1200px;
    height: 900px;
    overflow: hidden;
    background: var(--backdrop);
    font-family: "Raleway", sans-serif;
  }
  .canvas { position: relative; width: 1200px; height: 900px; }
  .card {
    position: absolute;
    border-radius: 4px;
    overflow: hidden;
    box-shadow: 0 12px 28px rgba(18, 42, 62, 0.4);
  }
  .card--front { left: 130px; top: 130px; width: 380px; height: 640px; }
  .card--back  { left: 570px; top: 280px; width: 540px; height: 320px; }
  .card__texture {
    position: absolute;
    inset: 0;
    background:
      radial-gradient(circle at 30% 25%, rgba(255,255,255,0.06) 0 18%, transparent 40%),
      radial-gradient(ellipse at 55% 40%, var(--card-light) 0%, var(--card-mid) 50%, var(--card-deep) 100%);
  }
  .card__art { position: absolute; inset: 0; width: 100%; height: 100%; }
  .wordmark {
    font-family: "Zilla Slab", serif;
    font-weight: 700;
    fill: var(--brand-green);
  }
  .tagline {
    font-family: "Raleway", sans-serif;
    font-weight: 800;
    fill: var(--brand-green);
    letter-spacing: 1px;
  }
  .brand-dot { fill: var(--brand-green); }
  .contact {
    position: absolute;
    top: 30px;
    right: 32px;
    list-style: none;
    text-align: right;
    color: var(--contact-white);
    font-weight: 300;
    font-size: 17px;
    line-height: 1.6;
  }
</style>
</head>
<body>
<main class="canvas">
  <section class="card card--front">
    <div class="card__texture" role="img" aria-label="Water droplets on a deep blue surface"></div>
    <svg class="card__art" viewBox="0 0 380 640" aria-label="Tallow Creek Plumbing and Gas">
      <defs>
        <path id="front-arc" d="M 30 300 Q 190 90 350 300"/>
      </defs>
      <text class="wordmark" font-size="50" text-anchor="middle">
        <textPath href="#front-arc" startOffset="50%">Tallow Creek</textPath>
      </text>
      <circle class="brand-dot" cx="190" cy="320" r="38"/>
      <text class="tagline" x="190" y="430" font-size="40" text-anchor="middle">PLUMBING</text>
      <text class="tagline" x="190" y="480" font-size="34" text-anchor="middle">&amp; GAS</text>
    </svg>
  </section>

  <section class="card card--back">
    <div class="card__texture" role="img" aria-label="Water droplets on a deep blue surface"></div>
    <ul class="contact">
      <li>Owner's Name</li>
      <li>Telephone Number</li>
      <li>Website (if any)</li>
      <li>Services/Skills Offered</li>
    </ul>
    <svg class="card__art" viewBox="0 0 540 320" aria-label="Tallow Creek">
      <defs>
        <path id="back-arc" d="M 30 270 Q 150 150 270 270"/>
      </defs>
      <text class="wordmark" font-size="34" text-anchor="middle">
        <textPath href="#back-arc" startOffset="50%">Tallow Creek</textPath>
      </text>
      <circle class="brand-dot" cx="150" cy="262" r="16"/>
    </svg>
  </section>
</main>
</body>
</html>
```